Advertisement Coaching practice

I need an advertisement (to be printed in newspaper). I have a coaching practice where I offer coaching, workshops family constellations and relationship therapy. The ad needs to express calmness, inspiration to transform but also not dull and boring. It would be great if you could use the colors from my logo into the ad.

Dimensions are: 13,04 cm Width x 9,72 cm Height.

I will add my previous self-made ad, my company logo, a portrait photo of myself and the text I want to add. Also my contact details should be visible as well.

Requirements
Nice to have
• I have updated the brief with a flyer that I had previously made by a designer. It would be a nice to have if the ad ties in with that. You can also look at my website at www.bravemoor.nu to see what colors I used there.

```html
<!DOCTYPE html>
<html lang="nl">
<head>
<meta charset="utf-8">
<title>Advertentie – Coaching, familieopstellingen &amp; relatietherapie</title>
<link href="https://fonts.googleapis.com/css2?family=Catamaran:wght@400;500&family=Mukta:wght@400&display=swap" rel="stylesheet">
<style>
  :root {
    --backdrop: #808080;
    --frame-teal: #7db8b2;
    --soft-teal: #bcdcdc;
    --mist-teal: #d6e9e8;
    --line-teal: #6fb0a8;
    --heading-teal: #6fb0a8;
    --ink: #555555;
    --ink-dark: #4a4a4a;
    --paper: #ffffff;
    --photo-dark: #5a5a5a;
    --photo-light: #cfcfcf;
  }
  * { margin: 0; padding: 0; box-sizing: border-box; }
  html, body { width: 1200px; height: 1200px; overflow: hidden; }
  body {
    background: var(--backdrop);
    position: relative;
    font-family: "Catamaran", "Mukta", sans-serif;
    color: var(--ink);
  }
  .ad {
    position: absolute;
    left: 57px; top: 195px;
    width: 1086px; height: 810px;
    background: var(--frame-teal);
  }
  .ad-shapes {
    position: absolute;
    left: 0; top: 0;
    width: 1200px; height: 1200px;
  }
  .ad-heading {
    position: absolute;
    left: 122px; top: 262px;
    font-weight: 400;
    font-size: 35px;
    line-height: 44px;
    letter-spacing: -1.6px;
    color: var(--heading-teal);
    text-transform: uppercase;
  }
  .ad-body {
    position: absolute;
    left: 122px; top: 429px;
    width: 680px;
    font-size: 21px;
    line-height: 27.5px;
    letter-spacing: -0.6px;
    color: var(--ink);
  }
  .ad-body p { margin-bottom: 27.5px; }
  .ad-body ul { list-style: none; }
  .ad-body li::before { content: "• "; font-size: 14px; }
  .portrait {
    position: absolute;
    left: 810px; top: 270px;
    width: 236px; height: 446px;
    border-radius: 118px;
    background: linear-gradient(170deg, var(--photo-dark) 0%, #7a7a7a 45%, var(--photo-light) 100%);
  }
  .contact {
    position: absolute;
    left: 138px; top: 840px;
    font-family: "Mukta", sans-serif;
    font-size: 24px;
    line-height: 35px;
    letter-spacing: -0.4px;
    color: var(--ink);
  }
  .brand {
    position: absolute;
    left: 812px; top: 746px;
    width: 270px;
    text-align: center;
  }
  .brand-mark {
    display: block;
    width: 88px; height: 88px;
    margin: 0 auto 10px;
    border-radius: 50%;
    border: 3px solid #888888;
  }
  .brand-name {
    font-family: "Catamaran", sans-serif;
    font-weight: 500;
    font-size: 52px;
    line-height: 56px;
    letter-spacing: 1px;
    color: var(--ink-dark);
  }
</style>
</head>
<body>
  <div class="ad"></div>

  <svg class="ad-shapes" viewBox="0 0 1200 1200" aria-hidden="true">
    <path d="M158 214 H1124 V906 Q1124 986 1044 986 H78 V294 Q78 214 158 214 Z" fill="var(--paper)"/>
    <path d="M652 214 C730 238 800 275 850 300 C900 320 960 360 1064 376 C1090 380 1110 384 1124 384 V214 Z" fill="var(--soft-teal)"/>
    <path d="M78 986 V904 C150 872 300 878 400 902 C480 922 520 958 544 986 Z" fill="var(--mist-teal)"/>
    <path d="M78 862 C180 850 260 890 300 930 C340 960 360 975 376 986" fill="none" stroke="var(--line-teal)" stroke-width="2"/>
    <path d="M648 986 C640 920 650 880 720 860 C820 830 880 790 892 712" fill="none" stroke="var(--line-teal)" stroke-width="2.5"/>
    <path d="M1046 454 C1080 470 1100 560 1108 700 C1114 820 1118 920 1122 984" fill="none" stroke="var(--line-teal)" stroke-width="2.5"/>
    <path d="M832 700 V378 A115 115 0 0 1 1062 378 V380" fill="none" stroke="var(--paper)" stroke-width="2.5"/>
  </svg>

  <h1 class="ad-heading">Coaching,<br>Familieopstellingen<br>&amp; Relatietherapie</h1>

  <div class="ad-body">
    <p>Trauma's en negatieve ervaringen vormen ons en blijven nog lang voelbaar. Ze kunnen groei of geluk in de weg staan.</p>
    <p style="margin-bottom:0">Ik ben Amara en ondersteun je bij het:</p>
    <ul style="margin-bottom:27.5px">
      <li>Doorbreken van belemmerende patronen;</li>
      <li>Beter omgaan met conflicten;</li>
      <li>In gezonde verbinding met elkaar als koppel of met anderen komen;</li>
    </ul>
    <p>Maandelijks geef ik workshops familieopstellingen. Ook houd ik themasessies rond adoptie, moeder-dochterdynamiek of relaties. Ook bied ik individuele coaching, relatietherapie en retraites aan. Kijk op de website voor meer info of neem contact op en ontdek wat het beste bij jou past.</p>
  </div>

  <div class="portrait" role="img" aria-label="Zwart-witportret van de coach"></div>

  <div class="contact">
    <div>Amara Veldkamp</div>
    <div>M: info@bravemoor.nu | T: 06-12 34 56 78</div>
    <div>www.bravemoor.nu</div>
  </div>

  <div class="brand">
    <span class="brand-mark"></span>
    <div class="brand-name">bravemoor</div>
  </div>
</body>
</html>
```